Wine labels Velmora Wine Council - Nueva etiqueta El Consejo Regulador de vinos de Albarrán

Velmora Wines Council, based in southern Spain, are looking to create a new suite of wine labels which retain the elegance of the Velmora Wines industry while reinvigorating their image to the modern era and a new generation of Sherry Wine lovers. These labels will be used across the Velmora Wines Council's range of wines for the promotion of the Velmora Wines industry.

Your design must present at least two styles of Velmora Wines which demonstrate an elegant, modern interpretation and understanding of the unique mood and personality for these wines and the essence of southern Spain.

10 labels will be created based on the winning design, one for each of the unique varieties of Velmora Wines within the collection. This collection comprises of several different wine varieties including: Fino, Manzanilla, Amontillado, Oloroso, Palo Cortado, Medium, Cream, Pale Cream, Pedro Ximenez and Moscatel.

We recommend you visit our website www.velmora-vinos.example/wines as the source to understanding the origins and unique personality of these diverse wines.

El Consejo Regulador de los Vinos de Albarrán y Tordesal quiere renovar las etiquetas de los vinos utilizados para sus actividades de promoción genérica. Esta colección de vinos comprende las tipologías más importantes de la región que incluye: fino, manzanilla, amontillado, oloroso, palo cortado, pale cream, medium, cream, pedro ximénez y moscatel. Por lo tanto se precisan 10 etiquetas, una para cada uno de los vinos mencionados.
Updates

Project Deadline Extended
Reason: Due to some confusion with the deadline we wish to officially extend the deadline to allow designers one last week to submit their entries.

Target Market(s)

Industry, journalists, media, sommeliers, chefs, wine writers

Industry/Entity Type

Council

Requirements
Must have
• Front and Back label plus capsule:
• Front label can have either of the two official logos of the Velmora Wine council titled Vinos de Albarrán Digital or not, this is optional. Must include: Vino selecionado por el Consejo Regulador de la Denominacion de Origen, Name of the variety of wine eg FINO, percentage of alcohol eg 15% and quantity 75 cl.
• The back of the label must include the council logo titled Sellora and 4 additional logos positioned smaller. The Europa logo must appear larger than the 3 other logos. Space for descriptive text about the wine is also required.
• The dimensions of the bottle can be found at this link http://www.vidrialto.example/es/catalogo/vinos-y-espumosos/bordelesas/bd-orla
• Altura:305 mm
• Diámetro base:76,20 mm
• Diámetro hombro:82 mm
• Tipo boca:Cetie
• Peso:750 gr
• Capacidad:75 cl
• Etiqueta delantera y trasera y capsula
• La etiqueta delantera puede incluir el logo oficial del Consejo Regulador o el logo digital, o ninguno, esto es opcional. Debe incluir el siguiete texto: Vino selecionado por el Consejo Regulador de la Denominacion de Origen, el nombre de la variedad del vino, por ejemplo Fino, el porcentaje de alcohol, por ejemplo 15%, y la capacidad 75cl.
• La etiqueta trasera debe incluir el logo oficial Sellora del Consejo, y cuatro logos adicionales con una dimension menor. El Logo de ¨Europa invierte en las zonas rurales¨ debe ser de mayor tamaño que los otros. Se precisa espacio para el texto descriptivo de los vinos.
• Las dimensiones de la botella se puede encontrar en este enlace
• http://www.vidrialto.example/es/catalogo/vinos-y-espumosos/bordelesas/bd-orla
• Altura:305 mm
• Diámetro base:76,20 mm
• Diámetro hombro:82 mm
• Tipo boca:Cetie
• Peso:750 gr
• Capacidad:75 cl
Nice to have
• See our website velmora-vinos.example to understand the origin of the wines. Ver nuestra página web velmora-vinos.example para mejor entender los vinos.
Should not have
• Images of catavinos or stereotypical images from Spain such as flamenco dancers or guitars.

```html
<!DOCTYPE html>
<html lang="es">
<head>
<meta charset="utf-8">
<title>Manzanilla – Velmora Wines label</title>
<link rel="stylesheet" href="https://fonts.googleapis.com/css2?family=Cormorant+Garamond:wght@500&family=Dancing+Script:wght@600&family=Roboto:wght@300;400&display=swap">
<style>
  :root {
    --backdrop: #5e5e60;
    --label-white: #ffffff;
    --ink: #231f20;
    --magenta: #c1266b;
    --plum: #7b2b5b;
  }
  * { box-sizing: border-box; margin: 0; padding: 0; }
  html, body {
    width: 1200px;
    height: 966px;
    overflow: hidden;
  }
  body {
    background: var(--backdrop);
    position: relative;
  }
  .front-label {
    position: absolute;
    left: 345px;
    top: 109px;
    width: 511px;
    height: 748px;
    background: var(--label-white);
    overflow: hidden;
  }
  .top-band {
    position: absolute;
    left: 0; top: 0;
    width: 100%;
    height: 30px;
    background: var(--magenta);
  }
  .brand-mark {
    position: absolute;
    left: 225px;
    top: 128px;
    width: 60px;
    height: 60px;
    border: 1.5px solid var(--ink);
    border-radius: 50%;
  }
  .brand {
    position: absolute;
    left: 0;
    top: 268px;
    width: 100%;
    text-align: center;
    color: var(--ink);
  }
  .brand-name {
    display: block;
    font-family: "Cormorant Garamond", serif;
    font-weight: 500;
    font-size: 46px;
    line-height: 1;
    letter-spacing: -1.2px;
  }
  .brand-sub {
    display: block;
    margin-top: 14px;
    font-family: "Roboto", sans-serif;
    font-weight: 300;
    font-size: 19px;
    letter-spacing: 3.5px;
  }
  .variety {
    position: absolute;
    left: 0;
    top: 388px;
    width: 100%;
    text-align: center;
    font-family: "Dancing Script", cursive;
    font-weight: 600;
    font-size: 90px;
    line-height: 1;
    color: var(--ink);
  }
  .selection-note {
    position: absolute;
    left: 0;
    top: 500px;
    width: 100%;
    text-align: center;
    font-family: "Roboto", sans-serif;
    font-weight: 300;
    font-size: 11px;
    letter-spacing: 0.3px;
    color: var(--ink);
  }
  .specs {
    position: absolute;
    left: 29px;
    right: 29px;
    top: 531px;
    display: flex;
    justify-content: space-between;
    font-family: "Roboto", sans-serif;
    font-weight: 400;
    font-size: 17px;
    color: var(--ink);
  }
  .landscape {
    position: absolute;
    left: 0;
    bottom: 0;
    width: 511px;
    height: 180px;
    display: block;
  }
</style>
</head>
<body>
  <main class="front-label">
    <div class="top-band"></div>

    <span class="brand-mark" aria-hidden="true"></span>

    <div class="brand">
      <span class="brand-name">VINOS DE ALBARRÁN</span>
      <span class="brand-sub">VELMORA WINES</span>
    </div>

    <h1 class="variety">Manzanilla</h1>

    <p class="selection-note">Vino seleccionado por el Consejo Regulador de la Denominación de Origen</p>

    <div class="specs">
      <span class="spec-alcohol">Alc.15%</span>
      <span class="spec-volume">75 cl.</span>
    </div>

    <svg class="landscape" viewBox="0 0 511 180" role="img" aria-label="Vineyard landscape with rolling hills and cypress trees in magenta and plum tones">
      <defs>
        <linearGradient id="vineyard-tone" x1="0" y1="0" x2="0" y2="1">
          <stop offset="0" stop-color="#7b2b5b"/>
          <stop offset="0.45" stop-color="#c1266b"/>
          <stop offset="1" stop-color="#a02460"/>
        </linearGradient>
      </defs>
      <path d="M0 18 C60 4 120 2 170 10 C220 0 270 -2 320 14 C380 2 450 0 511 12 L511 180 L0 180 Z" fill="url(#vineyard-tone)"/>
    </svg>
  </main>
</body>
</html>
```